The Timber Loft

We need a business card design for our wardrobe company.
Please visit our website www.zorvelcabinets.com to get an idea of who we are.

```html
<!DOCTYPE html>
<html lang="en">
<head>
<meta charset="utf-8">
<title>The Timber Loft – Business Card</title>
<link rel="stylesheet" href="https://fonts.googleapis.com/css2?family=Quicksand:wght@500;700&display=swap">
<style>
  :root {
    --backdrop: #3a3a3c;
    --card: #16161a;
    --gold: #c9a24e;
    --gold-soft: #b38c3e;
  }
  html, body {
    margin: 0;
    padding: 0;
    width: 1200px;
    height: 900px;
    overflow: hidden;
    background: var(--backdrop);
  }
  .canvas {
    position: relative;
    width: 1200px;
    height: 900px;
    font-family: "Quicksand", sans-serif;
  }
  .business-card {
    position: absolute;
    left: 180px;
    top: 210px;
    width: 840px;
    height: 480px;
    background: var(--card);
    box-shadow: 0 10px 30px rgba(0,0,0,0.45);
  }
  .brand-mark {
    position: absolute;
    left: 400px;
    top: 70px;
    width: 58px;
    height: 58px;
    border: 2px solid var(--gold);
    box-sizing: border-box;
  }
  .card-content {
    position: absolute;
    left: 250px;
    top: 150px;
    width: 440px;
    color: var(--gold);
  }
  .company-name {
    margin: 0;
    font-weight: 700;
    font-size: 24px;
    letter-spacing: 0.5px;
    text-transform: uppercase;
    text-align: center;
  }
  .tagline {
    margin: 4px 0 0;
    font-weight: 700;
    font-size: 22px;
    text-align: center;
  }
  .contact-list {
    list-style: none;
    margin: 12px 0 0;
    padding: 0;
    font-weight: 500;
    font-size: 18px;
  }
  .contact-line {
    padding: 9px 0;
    white-space: nowrap;
  }
  .rule {
    display: block;
    height: 1px;
    background: var(--gold-soft);
  }
  .rule--phone   { margin-left: 40px; width: 420px; }
  .rule--address { margin-left: 0;    width: 400px; }
  .rule--web     { margin-left: 60px; width: 360px; }
  .contact-line--web { padding-left: 10px; }
</style>
</head>
<body>
<main class="canvas">
  <section class="business-card" aria-label="The Timber Loft business card">
    <span class="brand-mark" aria-hidden="true"></span>
    <div class="card-content">
      <h1 class="company-name">The Timber Loft</h1>
      <p class="tagline">Crafted Square and True</p>
      <ul class="contact-list">
        <li><span class="rule rule--phone"></span></li>
        <li class="contact-line">0207 555 0148 | info@zorvelcabinets.com</li>
        <li><span class="rule rule--address"></span></li>
        <li class="contact-line">Alder Court, 42 Mill Lane, London EC2A 4RT</li>
        <li><span class="rule rule--web"></span></li>
        <li class="contact-line contact-line--web">www.zorvelcabinets.com</li>
      </ul>
    </div>
  </section>
</main>
</body>
</html>
```